Health Coach needs a creative and catchy Chatnook Ad Image to increase page likes

I have just recently launched a health coaching business and would like to increase my Chatnook awareness and page likes.
I plan on doing a “page liking” campaign through Chatnook and want a creative, catchy and unique image to help make my campaign successful.
I want a versatile image, as I am aiming to run this campaign on Chatnook for a while (few months).
The image is to be 1200 x 444 pixels, with an image ratio of 8:3, and because it is going on Chatnook it cannot have any overlaid text (or very little).
So, the image will have to be very visually appealing and catchy!
I am happy for some creative illustrations and drawings to be used to help portray my message (please see attached for some sample pictures)
I would like the image to portray the following:
-health
-happiness
-change
Some of my key messages that you could include:
-holistic health
-health & wellness
-health, nutrition, lifestyle
-Food, fitness, happiness

In addition, a call to action that could be incorporated could be:
"i can help you"
..or something similar (but only if this can fit).

I have attached some images of myself to be used.

Target Market(s)

People looking for health and fitness advice

Industry/Entity Type

Health And Wellness

Colors

Requirements
Nice to have
• illustrations as per 2 sample images provided
• call to action if can fit

```html
<!DOCTYPE html>
<html lang="en">
<head>
<meta charset="utf-8">
<title>Health Coach – I Can Help You</title>
<link rel="stylesheet" href="https://fonts.googleapis.com/css2?family=Oswald:wght@400;500&family=Bebas+Neue&display=swap">
<style>
  :root {
    --foliage-dark: #1f3a1c;
    --foliage-mid: #3f6b2f;
    --foliage-light: #7fa552;
    --stair-grey: #8e9386;
    --white: #ffffff;
    --happiness: #d97a8b;
    --fitness: #6f93c9;
    --lifestyle: #f7a23c;
    --nutrition: #e25b5b;
    --holistic: #a2dad1;
    --wellness: #9a4a6c;
  }
  * { margin: 0; padding: 0; box-sizing: border-box; }
  html, body { width: 1200px; height: 444px; overflow: hidden; background: var(--foliage-dark); }
  .banner {
    position: relative;
    width: 1200px;
    height: 444px;
    overflow: hidden;
    font-family: "Oswald", sans-serif;
  }
  .banner__scene {
    position: absolute;
    inset: 0;
    background:
      radial-gradient(ellipse 260px 300px at 390px 260px, rgba(232,222,205,0.55), transparent 70%),
      radial-gradient(ellipse 500px 260px at 820px 120px, var(--foliage-light), transparent 75%),
      linear-gradient(100deg, var(--stair-grey) 0%, var(--foliage-mid) 18%, var(--foliage-dark) 45%, var(--foliage-mid) 70%, var(--foliage-dark) 100%);
  }
  .topic {
    position: absolute;
    border-radius: 50%;
    display: flex;
    align-items: center;
    justify-content: center;
    text-align: center;
    color: var(--white);
    font-weight: 500;
    text-transform: uppercase;
    line-height: 1.1;
    letter-spacing: 0.5px;
  }
  .topic--happiness { left: 123px; top: 58px;  width: 140px; height: 140px; background: var(--happiness); font-size: 22px; }
  .topic--fitness   { left: 35px;  top: 302px; width: 106px; height: 106px; background: var(--fitness);   font-size: 19px; }
  .topic--lifestyle { left: 790px; top: -25px; width: 150px; height: 150px; background: var(--lifestyle); font-size: 28px; }
  .topic--nutrition { left: 1053px; top: 108px; width: 108px; height: 108px; background: var(--nutrition); font-size: 18px; }
  .topic--holistic  { left: 898px; top: 208px; width: 140px; height: 140px; background: var(--holistic); font-size: 24px; }
  .topic--wellness  { left: 1066px; top: 350px; width: 102px; height: 102px; background: var(--wellness); font-size: 18px; }
  .headline {
    position: absolute;
    left: 490px;
    top: 140px;
    width: 250px;
    text-align: center;
    font-family: "Bebas Neue", sans-serif;
    font-size: 74px;
    line-height: 0.92;
    letter-spacing: 3px;
    color: var(--white);
  }
</style>
</head>
<body>
  <main class="banner">
    <div class="banner__scene" role="img" aria-label="Photo of the smiling health coach in a white sleeveless top leaning on a white stair railing in front of a green hedge, with hand-drawn white doodles of leaves, a dumbbell, a carrot, a steaming coffee cup, an alarm clock and a sunburst around the headline"></div>

    <div class="topic topic--happiness">Happiness</div>
    <div class="topic topic--fitness">Fitness</div>
    <div class="topic topic--lifestyle">Lifestyle</div>
    <div class="topic topic--nutrition">Nutrition</div>
    <div class="topic topic--holistic">Holistic<br>Health</div>
    <div class="topic topic--wellness">Wellness</div>

    <h1 class="headline">I Can<br>Help<br>You.</h1>
  </main>
</body>
</html>
```